RTW Business Card Design

We are an independent auto dealer who specializes in commercial & fleet vehicles, we are family owned and operated and have been in business since 2001. We stock late model, low mileage, white trucks & vans. We mostly deal with companies in the construction and service industries. We are just looking to try to freshen up our old business card, we do not want to change the logo at this point, because it is well know within the southwest region & construction community. I have attached our logo and a PDF of our current business card for reference.
Updates
If the address is stacked there is no comma (,) after NE. Everyone keeps putting it in with this format and it is not correct.
842 Ventana Blvd NE
Albuquerque, NM 87120
If the address is all on one line, then there will be a comma (,) after NE
842 Ventana Blvd NE, Albuquerque, NM 87120
Please make changes accordingly, thank you for your attention in this matter.
Industry/Entity Type
Construction
Contact Information for Business Card
842 Ventana Blvd NE, Albuquerque, NM 87120, Marcus Delaney, Vice President, marcus@rtwvehicledepot.com, www.RTWvehicledepot.com, ph 505-610-2247, fax 505-472-8156, cell 505-238-6094
Look and feel
Each slider illustrates characteristics of the customer's brand and the style your logo design should communicate.

```html
<!DOCTYPE html>
<html lang="en">
<head>
<meta charset="utf-8">
<title>RTW Vehicle Depot — Business Card</title>
<link rel="stylesheet" href="https://fonts.googleapis.com/css2?family=Cinzel:wght@400;700&display=swap">
<style>
  :root {
    --stage: #d9d6d1;
    --card-black: #141414;
    --card-black-hi: #262626;
    --accent-red: #d8141c;
    --text-white: #f1f1f1;
    --text-soft: #cfcfcf;
    --rule: #bdbdbd;
  }
  * { margin: 0; padding: 0; box-sizing: border-box; }
  html, body {
    width: 1200px; height: 600px; overflow: hidden;
    background: var(--stage);
  }
  .stage {
    width: 1200px; height: 600px;
    display: flex; align-items: center; justify-content: center;
  }
  .business-card {
    position: relative;
    width: 840px; height: 480px;
    background: linear-gradient(160deg, var(--card-black-hi) 0%, var(--card-black) 45%, #0b0b0b 100%);
    font-family: "Cinzel", "Times New Roman", serif;
    color: var(--text-white);
    box-shadow: 0 14px 30px rgba(0,0,0,0.35);
    overflow: hidden;
  }
  .identity {
    position: absolute; right: 60px; top: 62px;
    text-align: right;
  }
  .identity__name {
    color: var(--accent-red);
    font-weight: 700;
    font-size: 30px;
    letter-spacing: 1px;
  }
  .identity__title {
    color: var(--text-white);
    font-size: 18px;
    margin-top: 4px;
    letter-spacing: 0.5px;
  }
  .rule {
    position: absolute; height: 2px; background: var(--rule);
  }
  .rule--upper { left: 330px; right: 60px; top: 152px; }
  .rule--lower { left: 60px; width: 470px; top: 312px; }
  .address {
    position: absolute; right: 60px; top: 172px;
    text-align: right; font-size: 18px; line-height: 30px;
    color: var(--text-soft);
  }
  .brand-name {
    position: absolute; left: 60px; top: 228px;
    font-size: 40px; font-weight: 700;
    color: var(--text-white);
    letter-spacing: 1px;
  }
  .contact-list {
    position: absolute; left: 60px; top: 330px;
    list-style: none; font-size: 17px; line-height: 27px;
    color: var(--text-soft);
  }
  .contact-list li { display: flex; align-items: center; gap: 12px; }
  .contact-list svg { width: 16px; height: 16px; flex: none; }
  .web-band {
    position: absolute; right: 0; bottom: 0;
    width: 250px; height: 58px;
    background: var(--accent-red);
    display: flex; align-items: center; justify-content: center;
    font-size: 16px; color: var(--text-white);
    letter-spacing: 0.5px;
  }
</style>
</head>
<body>
<main class="stage">
  <article class="business-card">
    <header class="identity">
      <p class="identity__name">Marcus Delaney</p>
      <p class="identity__title">Vice President</p>
    </header>
    <div class="rule rule--upper"></div>
    <address class="address">
      842 Ventana Blvd NE<br>
      Albuquerque, NM 87120
    </address>

    <p class="brand-name">RTW Vehicle Depot</p>
    <div class="rule rule--lower"></div>

    <ul class="contact-list">
      <li>
        <svg viewBox="0 0 16 16" aria-hidden="true"><rect width="16" height="16" fill="var(--accent-red)"/><rect x="5" y="2.5" width="6" height="11" rx="1" fill="none" stroke="#fff" stroke-width="1.4"/></svg>
        <span>505-238-6094</span>
      </li>
      <li>
        <svg viewBox="0 0 16 16" aria-hidden="true"><rect width="16" height="16" fill="var(--accent-red)"/><path d="M4 3.5c0 5 3.5 8.5 8.5 8.5l0.5-2.2-2.4-1-1.1 1.2c-1.5-.7-2.4-1.6-3.1-3.1l1.2-1.1-1-2.4z" fill="#fff"/></svg>
        <span>505-610-2247</span>
      </li>
      <li>
        <svg viewBox="0 0 16 16" aria-hidden="true"><rect width="16" height="16" fill="var(--accent-red)"/><rect x="3" y="6.5" width="10" height="6" fill="#fff"/><rect x="5" y="3" width="6" height="4" fill="none" stroke="#fff" stroke-width="1.2"/></svg>
        <span>505-472-8156</span>
      </li>
      <li>
        <svg viewBox="0 0 16 16" aria-hidden="true"><rect width="16" height="16" fill="var(--accent-red)"/><rect x="3" y="4.5" width="10" height="7" fill="none" stroke="#fff" stroke-width="1.2"/><path d="M3 4.5l5 4 5-4" fill="none" stroke="#fff" stroke-width="1.2"/></svg>
        <span>marcus@rtwvehicledepot.com</span>
      </li>
    </ul>

    <footer class="web-band">www.RTWvehicledepot.com</footer>
  </article>
</main>
</body>
</html>
```